Ridgeway Ore Advisory Business Card

Ridgeway Ore Advisory is a company that provides consulting services to the Mining Industry.

Whilst Ridgeway Ore Advisory is an Australian based company its client base is the global mining industry.

The essence of Ridgeway Ore Advisory is its a can do organisation that can make a difference to its clients by providing quality assistance and form lasting relationships.
Updates

Target Market(s)

The global Mining Industry.

Industry/Entity Type

Mining

Font styles to use
Serif

Colors

Designer to choose colors to be used in the design.

Requirements
Nice to have
• My thinking is the card would look good in black given the logo.

I would like to see written on the back side of the card " Providing Metallurgical, Management and Corporate Services to the Mining Industry"

```html
<!DOCTYPE html>
<html lang="en">
<head>
<meta charset="utf-8">
<title>Ridgeway Ore Advisory – Business Card</title>
<link rel="stylesheet" href="https://fonts.googleapis.com/css2?family=Roboto+Slab:wght@400;700&display=swap">
<style>
  :root {
    --stage: #2a2624;
    --card-black: #141414;
    --card-white: #ffffff;
    --amber: #f5a623;
    --text-light: #e6e6e6;
    --text-muted: #b5b5b5;
  }
  html, body {
    margin: 0;
    width: 1200px;
    height: 716px;
    overflow: hidden;
    background: var(--stage);
    font-family: "Roboto Slab", Georgia, serif;
  }
  .canvas {
    position: relative;
    width: 1200px;
    height: 716px;
  }
  .card {
    position: absolute;
    top: 210px;
    width: 520px;
    height: 297px;
    overflow: hidden;
    box-shadow: 0 18px 40px rgba(0,0,0,.55);
  }
  .card--front { left: 50px; background: var(--card-black); }
  .card--back  { left: 630px; background: var(--card-black); }

  .front-split { position: absolute; inset: 0; }

  .wordmark {
    font-family: "Roboto Slab", Georgia, serif;
    font-weight: 700;
    color: var(--amber);
    text-transform: uppercase;
    line-height: 1;
    letter-spacing: .5px;
    margin: 0;
  }
  .card--front .wordmark {
    position: absolute;
    left: 48px;
    top: 40px;
    font-size: 34px;
  }
  .card--back .wordmark {
    position: absolute;
    right: 34px;
    top: 96px;
    font-size: 38px;
    text-align: right;
  }
  .tagline {
    position: absolute;
    right: 34px;
    top: 190px;
    width: 300px;
    margin: 0;
    text-align: right;
    font-size: 11px;
    line-height: 1.5;
    color: var(--text-light);
  }

  .holder {
    position: absolute;
    left: 20px;
    top: 172px;
  }
  .holder__name {
    display: flex;
    align-items: center;
    gap: 8px;
    color: var(--amber);
    font-weight: 700;
    font-size: 16px;
    margin: 0;
  }
  .holder__title {
    color: var(--amber);
    font-size: 10px;
    margin: 1px 0 8px 30px;
  }
  .contact-list {
    list-style: none;
    margin: 0;
    padding: 0;
    font-size: 9.5px;
    color: var(--text-light);
  }
  .contact-list li {
    display: flex;
    align-items: center;
    gap: 6px;
    margin-bottom: 5px;
  }
  .contact-list .address { margin-top: 8px; margin-left: 18px; }
  .icon {
    width: 11px;
    height: 11px;
    flex: none;
  }

  .company-info {
    position: absolute;
    right: 20px;
    bottom: 16px;
    text-align: right;
    font-size: 9.5px;
    color: var(--text-light);
  }
  .company-info__label {
    color: var(--amber);
    font-size: 10.5px;
    margin: 0 0 6px;
    text-transform: uppercase;
  }
  .company-info__row {
    display: flex;
    justify-content: flex-end;
    align-items: center;
    gap: 6px;
    margin-bottom: 4px;
  }
</style>
</head>
<body>
<main class="canvas">

  <section class="card card--front" aria-label="Card front">
    <svg class="front-split" viewBox="0 0 520 297" aria-hidden="true">
      <rect width="520" height="297" fill="var(--card-black)"/>
      <polygon points="0,0 520,0 520,185 0,140" fill="var(--card-white)"/>
      <line x1="0" y1="143" x2="520" y2="188" stroke="var(--amber)" stroke-width="3"/>
    </svg>

    <h1 class="wordmark">Ridgeway<br>Ore Advisory</h1>

    <div class="holder">
      <p class="holder__name">
        <svg class="icon" viewBox="0 0 22 12" style="width:22px;height:12px" aria-hidden="true">
          <polyline points="1,1 6,6 1,11" fill="none" stroke="var(--amber)" stroke-width="2.2"/>
          <polyline points="9,1 14,6 9,11" fill="none" stroke="var(--amber)" stroke-width="2.2"/>
        </svg>
        Your Name
      </p>
      <p class="holder__title">Your Title</p>
      <ul class="contact-list">
        <li>
          <svg class="icon" viewBox="0 0 12 12" aria-hidden="true"><rect width="12" height="12" rx="2" fill="var(--amber)"/><rect x="4" y="2" width="4" height="8" rx="1" fill="var(--card-black)"/></svg>
          0123 456 789
        </li>
        <li>
          <svg class="icon" viewBox="0 0 12 12" aria-hidden="true"><rect width="12" height="12" rx="2" fill="var(--amber)"/><rect x="2" y="3.5" width="8" height="5" fill="none" stroke="var(--card-black)" stroke-width="1"/><polyline points="2,3.5 6,6.5 10,3.5" fill="none" stroke="var(--card-black)" stroke-width="1"/></svg>
          yourmail@ridgewayoreadvisory.com
        </li>
        <li class="address">
          <svg class="icon" viewBox="0 0 12 12" aria-hidden="true"><rect width="12" height="12" rx="2" fill="var(--amber)"/><path d="M6 2a2.5 2.5 0 0 1 2.5 2.5C8.5 6.5 6 10 6 10S3.5 6.5 3.5 4.5A2.5 2.5 0 0 1 6 2z" fill="var(--card-black)"/></svg>
          1100 Unknown Street, Anywhere, Australia
        </li>
      </ul>
    </div>

    <div class="company-info">
      <p class="company-info__label">Ridgeway Ore Advisory:</p>
      <div class="company-info__row">
        0123 456 789
        <svg class="icon" viewBox="0 0 12 12" aria-hidden="true"><rect width="12" height="12" rx="2" fill="var(--amber)"/><path d="M3 3l2-1 1 2-1 1a5 5 0 0 0 2 2l1-1 2 1-1 2C6 9 3 6 3 3z" fill="var(--card-black)"/></svg>
      </div>
      <div class="company-info__row">
        www.ridgewayoreadvisory.com
        <svg class="icon" viewBox="0 0 12 12" aria-hidden="true"><rect width="12" height="12" rx="2" fill="var(--amber)"/><circle cx="6" cy="6" r="3.5" fill="none" stroke="var(--card-black)" stroke-width="1"/><line x1="2.5" y1="6" x2="9.5" y2="6" stroke="var(--card-black)" stroke-width="1"/><ellipse cx="6" cy="6" rx="1.5" ry="3.5" fill="none" stroke="var(--card-black)" stroke-width="1"/></svg>
      </div>
    </div>
  </section>

  <section class="card card--back" aria-label="Card back">
    <h2 class="wordmark">Ridgeway<br>Ore Advisory</h2>
    <p class="tagline">Providing Metallurgical, Management and Corporate Services to the Mining Industry</p>
  </section>

</main>
</body>
</html>
```